showcase project portfolio

create power point of project portfolio
from word file and website using similar design template

https://www.brelvon.co.uk/

Target Market(s)

corporte

```html
<!DOCTYPE html>
<html lang="en">
<head>
<meta charset="utf-8">
<title>Brelvon Design – Project Portfolio</title>
<link href="https://fonts.googleapis.com/css2?family=Poppins:wght@400;500;600;700&display=swap" rel="stylesheet">
<style>
:root{
  --tan:#cfaa8b;
  --tan-line:#c99f7f;
  --navy:#1f3a4d;
  --ink:#2b2b2b;
  --muted:#555;
  --paper:#ffffff;
  --cream:#f4f1ec;
  --dark:#2a2d30;
}
*{margin:0;padding:0;box-sizing:border-box}
html,body{width:1200px;height:809px;overflow:hidden;background:var(--paper)}
body{position:relative;font-family:"Poppins",sans-serif;color:var(--ink)}
.icons{position:absolute;width:0;height:0}
.slide{position:absolute;width:349px;height:196px;background:var(--paper);overflow:hidden;box-shadow:0 3px 10px rgba(0,0,0,.16)}
.brand-mark{position:absolute;top:12px;right:8px;font-size:6px;font-weight:700;color:var(--navy);letter-spacing:.4px}
.slide-head{position:absolute;top:9px;left:0;width:100%;text-align:center}
.slide-head::before{content:"";display:block;width:12px;height:1.2px;background:#e8874a;margin:0 auto 3px}
.slide-title{font-size:10px;font-weight:700;line-height:1.15}
.slide-location{font-size:6.6px;font-weight:500;margin-top:1px}
.slide-proposal{font-size:5.1px;color:var(--muted);margin:5px auto 0;line-height:1.45;width:240px}
.slide-foot{position:absolute;left:0;bottom:0;width:100%;height:18px}
.foot-band{position:absolute;left:0;top:0;width:324px;height:18px;background:var(--tan);display:flex;align-items:center;padding-left:9px;gap:4px;font-size:5px;font-weight:600;color:#222}
.foot-band svg{width:8px;height:8px}
.page-no{position:absolute;right:4px;top:6px;font-size:4.6px;color:#333}
.shot{position:absolute;border:1.6px solid var(--tan-line);border-radius:1px}
.photo-brick{background:linear-gradient(135deg,#8a5a44 0%,#6a4b3d 50%,#7d8a6a 100%)}
.photo-lane{background:linear-gradient(120deg,#9aa7b3 0%,#7b5444 35%,#5d6a48 100%)}
.photo-tree{background:linear-gradient(160deg,#5f7040 0%,#8c5c45 55%,#b8b4a8 100%)}
.photo-plot{background:linear-gradient(180deg,#cfd8de 0%,#4f6a35 35%,#3d5229 80%,#8a8a82 100%)}
.photo-house{background:linear-gradient(180deg,#c8d3db 0%,#7a4a3a 45%,#5b4a44 80%,#9a958c 100%)}
.photo-sky{background:linear-gradient(180deg,#8fb0d6 0%,#9a5f48 40%,#6b5246 100%)}
.plan{background:linear-gradient(180deg,#f8f8f3 0%,#e4e4da 100%)}
.plan-yellow{background:linear-gradient(180deg,#fbf9e0 0%,#efea9a 50%,#f6f3cf 100%)}
/* cover */
.cover{background:var(--cream)}
.cover svg.cover-art{position:absolute;inset:0}
.cover-brand{position:absolute;top:62px;width:100%;text-align:center;color:#fff;font-size:13px;font-weight:700;letter-spacing:1.5px}
.cover-tag{position:absolute;top:100px;width:100%;text-align:center;color:#fff;font-size:11px;font-weight:500}
.contact-row{position:absolute;left:0;width:100%;display:flex;justify-content:space-around;padding:0 30px;font-size:6.4px;font-weight:500}
.contact-row span{display:flex;align-items:center;gap:3px}
.contact-row svg{width:10px;height:10px}
.cover .contact-row{top:166px;color:#222}
.copyright{position:absolute;top:184px;width:100%;text-align:center;font-size:4.4px;color:#333}
.cover-rule{position:absolute;left:0;top:181px;width:100%;height:.6px;background:#ddd6cc}
/* tasks */
.tasks{position:absolute;top:52px;display:flex;flex-direction:column;gap:4.4px;list-style:none;font-size:4.9px;line-height:7px;color:#333;white-space:nowrap}
.tasks li{display:flex;align-items:center;gap:3.5px}
.tasks li::before{content:"";flex:none;width:3px;height:3px;border:1px solid #444;border-radius:50%}
.tasks.left{left:13px}.tasks.right{left:164px}
/* thank you */
.thanks{background:var(--dark)}
.thanks-photo{position:absolute;inset:0;background:linear-gradient(180deg,#3a3c3a,#2c3033 60%,#232629)}
.thanks-brand{position:absolute;top:88px;width:100%;text-align:center;color:#fff;font-size:15px;font-weight:700;letter-spacing:1.6px}
.thanks-band{position:absolute;top:124px;left:0;width:100%;height:31px;background:var(--tan);display:flex;align-items:center;justify-content:center;color:#fff;font-size:19px;font-weight:700}
.thanks .contact-row{top:170px;color:#fff}
</style>
</head>
<body>

<svg class="icons" aria-hidden="true">
  <symbol id="ico-globe" viewBox="0 0 20 20"><circle cx="10" cy="10" r="10" fill="currentColor"/><circle cx="10" cy="10" r="5.5" fill="none" stroke="#444" stroke-width="1.1"/><ellipse cx="10" cy="10" rx="2.4" ry="5.5" fill="none" stroke="#444" stroke-width="1"/><path d="M4.5 10h11" stroke="#444" stroke-width="1"/></symbol>
  <symbol id="ico-globe-light" viewBox="0 0 20 20"><circle cx="10" cy="10" r="10" fill="currentColor"/><circle cx="10" cy="10" r="5.5" fill="none" stroke="#fff" stroke-width="1.1"/><ellipse cx="10" cy="10" rx="2.4" ry="5.5" fill="none" stroke="#fff" stroke-width="1"/><path d="M4.5 10h11" stroke="#fff" stroke-width="1"/></symbol>
  <symbol id="ico-mail" viewBox="0 0 20 20"><circle cx="10" cy="10" r="10" fill="currentColor"/><rect x="5" y="6.5" width="10" height="7" rx="1" fill="#fff"/><path d="M5.5 7l4.5 3.5L14.5 7" fill="none" stroke="currentColor" stroke-width="1"/></symbol>
  <symbol id="ico-phone" viewBox="0 0 20 20"><circle cx="10" cy="10" r="10" fill="currentColor"/><path d="M7 5.5l1.8 2.3-1 1.3a6 6 0 0 0 3.1 3.1l1.3-1 2.3 1.8-1 1.5c-4 .2-7.7-3.5-7.5-7.5z" fill="#fff"/></symbol>
</svg>

<!-- Cover -->
<section class="slide cover" style="left:33px;top:52px">
  <svg class="cover-art" viewBox="0 0 349 196" width="349" height="196">
    <path d="M0 0H349V104C300 134 240 147 175 146C105 145 45 130 0 110Z" fill="#3a3836" role="img" aria-label="Photograph of a corner brick building, darkened"/>
    <path d="M75 145C160 158 270 150 349 105" fill="none" stroke="var(--tan)" stroke-width="4"/>
  </svg>
  <div class="cover-brand">BRELVON DESIGN</div>
  <div class="cover-tag">ARCHITECTURE TODAY, READY FOR TOMORROW</div>
  <div class="contact-row">
    <span><svg style="color:var(--navy)"><use href="#ico-globe-light"/></svg>www.brelvon.co.uk</span>
    <span><svg style="color:var(--navy)"><use href="#ico-mail"/></svg>info@brelvon.co.uk</span>
    <span><svg style="color:var(--navy)"><use href="#ico-phone"/></svg>+44 7700 900418</span>
  </div>
  <div class="cover-rule"></div>
  <div class="copyright">© 2024. ALL Rights Reserved.</div>
</section>

<!-- Tasks -->
<section class="slide" style="left:424px;top:52px">
  <div class="brand-mark">BRELVON</div>
  <header class="slide-head" style="top:17px"><h2 class="slide-title">Tasks</h2></header>
  <ul class="tasks left">
    <li>Creating working drawings</li>
    <li>Price breakdown of total build costs</li>
    <li>Liaising with Ridgeway waters for water connection,</li>
    <li>drainage connection</li>
    <li>Liaising with Northmere gas to get gas supply to site</li>
    <li>Liaising with Meridian Power to get electric supply</li>
    <li>Tendering out works to different tradesman</li>
    <li>Getting material orders</li>
  </ul>
  <ul class="tasks right">
    <li>Arranging structural engineer for the site</li>
    <li>Arranging Building control for the site</li>
    <li>Making sure material is on site on time</li>
    <li>Making sure all tradesman work is up to current British standards</li>
    <li>Daily walk rounds to check work is done according to approved plans</li>
    <li>Placing orders for bathrooms, kitchen, and flooring</li>
    <li>All snag work with main contactor</li>
  </ul>
  <footer class="slide-foot"><div class="foot-band"><svg style="color:#fff"><use href="#ico-globe"/></svg>www.brelvon.co.uk</div><span class="page-no">Page 02</span></footer>
</section>

<!-- Project 1 -->
<section class="slide" style="left:814px;top:52px">
  <div class="brand-mark">BRELVON</div>
  <header class="slide-head">
    <h2 class="slide-title">Project 1</h2>
    <p class="slide-location">Garages at Aldermoor Mews, Aldermoor Street, Kestford</p>
    <p class="slide-proposal">Proposal: Change of use from garages to two dwelling houses (use class C3) including alterations to the front and side elevations</p>
  </header>
  <div class="shot photo-lane" style="left:6px;top:64px;width:98px;height:76px" role="img" aria-label="Photo of existing brick garages along a lane"></div>
  <div class="shot plan-yellow" style="left:117px;top:64px;width:116px;height:98px" role="img" aria-label="Floor plans and elevations drawing sheet"></div>
  <div class="shot photo-brick" style="left:246px;top:64px;width:92px;height:76px" role="img" aria-label="Photo of the completed brick houses"></div>
  <footer class="slide-foot"><div class="foot-band"><svg style="color:#fff"><use href="#ico-globe"/></svg>www.brelvon.co.uk</div><span class="page-no">Page 03</span></footer>
</section>

<!-- Project 2 -->
<section class="slide" style="left:33px;top:306px">
  <div class="brand-mark">BRELVON</div>
  <header class="slide-head">
    <h2 class="slide-title">Project 2</h2>
    <p class="slide-location">Location: 48 Fennick Road, Kestford</p>
    <p class="slide-proposal" style="width:300px">Proposal: Change of use from offices (use class B1) to 12 flats (use class C3)</p>
  </header>
  <div class="shot photo-tree" style="left:5px;top:63px;width:114px;height:69px" role="img" aria-label="Photo of brick office building behind a large tree"></div>
  <div class="shot photo-tree" style="left:124px;top:63px;width:114px;height:69px" role="img" aria-label="Photo of the building front and courtyard"></div>
  <div class="shot plan" style="left:243px;top:63px;width:98px;height:69px" role="img" aria-label="Floor plan drawing sheet for the flats"></div>
  <footer class="slide-foot"><div class="foot-band"><svg style="color:#fff"><use href="#ico-globe"/></svg>www.brelvon.co.uk</div><span class="page-no">Page 04</span></footer>
</section>

<!-- Project 3 -->
<section class="slide" style="left:424px;top:306px">
  <div class="brand-mark">BRELVON</div>
  <header class="slide-head">
    <h2 class="slide-title">Project 3</h2>
    <p class="slide-location">Location: 12-16 Market Row Kestford</p>
    <p class="slide-proposal" style="width:230px">Proposal: Refurbishment Of Commercial Ground Floor Units Together With Formation Of 6 Residential Units On First And Second Floors. Installation Of Glazing And Repair To External Masonry Including Bricking Up Of Existing Openings</p>
  </header>
  <div class="shot plan-yellow" style="left:66px;top:72px;width:216px;height:87px" role="img" aria-label="Colour-coded floor plans for ground, first and second floors"></div>
  <footer class="slide-foot"><div class="foot-band"><svg style="color:#fff"><use href="#ico-globe"/></svg>www.brelvon.co.uk</div><span class="page-no">Page 05</span></footer>
</section>

<!-- Project 4 -->
<section class="slide" style="left:814px;top:306px">
  <div class="brand-mark">BRELVON</div>
  <header class="slide-head">
    <h2 class="slide-title">Project 4</h2>
    <p class="slide-location">Location: Land At 3 Brookfield Kestford KF4 2QJ</p>
    <p class="slide-proposal" style="margin-top:3px">Proposal: Erection of a dwelling house (use class C3)</p>
  </header>
  <div class="shot photo-plot" style="left:61px;top:49px;width:97px;height:51px" role="img" aria-label="Photo of the overgrown empty plot"></div>
  <div class="shot photo-house" style="left:188px;top:49px;width:79px;height:51px" role="img" aria-label="Photo of the finished brick house"></div>
  <div class="shot plan" style="left:61px;top:109px;width:76px;height:63px" role="img" aria-label="Site and floor plan drawings"></div>
  <div class="shot plan" style="left:161px;top:109px;width:107px;height:63px" role="img" aria-label="Proposed front elevation drawing"></div>
  <footer class="slide-foot"><div class="foot-band"><svg style="color:#fff"><use href="#ico-globe"/></svg>www.brelvon.co.uk</div><span class="page-no">Page 06</span></footer>
</section>

<!-- Project 5 -->
<section class="slide" style="left:228px;top:560px">
  <div class="brand-mark">BRELVON</div>
  <header class="slide-head">
    <h2 class="slide-title">Project 5</h2>
    <p class="slide-location">Location: 19, Carden Street, Halbury</p>
    <p class="slide-proposal" style="margin-top:3px">Proposal: Warehouse conversion to 4 town houses.</p>
  </header>
  <div class="shot photo-brick" style="left:17px;top:83px;width:71px;height:81px" role="img" aria-label="Photo of the warehouse frontage before works"></div>
  <div class="shot photo-house" style="left:94px;top:58px;width:62px;height:79px" role="img" aria-label="Photo of the converted frontage"></div>
  <div class="shot plan" style="left:162px;top:83px;width:100px;height:79px" role="img" aria-label="Town house floor plans"></div>
  <div class="shot photo-sky" style="left:269px;top:58px;width:60px;height:78px" role="img" aria-label="Photo of the rear courtyard and brick walls"></div>
  <footer class="slide-foot"><div class="foot-band"><svg style="color:#fff"><use href="#ico-globe"/></svg>www.brelvon.co.uk</div><span class="page-no">Page 07</span></footer>
</section>

<!-- Thank you -->
<section class="slide thanks" style="left:619px;top:560px">
  <div class="thanks-photo" role="img" aria-label="Darkened photograph of a street with houses"></div>
  <div class="thanks-brand">BRELVON DESIGN</div>
  <div class="thanks-band">Thank You</div>
  <div class="contact-row">
    <span><svg style="color:var(--tan)"><use href="#ico-globe-light"/></svg>www.brelvon.co.uk</span>
    <span><svg style="color:var(--tan)"><use href="#ico-mail"/></svg>info@brelvon.co.uk</span>
    <span><svg style="color:var(--tan)"><use href="#ico-phone"/></svg>+44 7700 900418</span>
  </div>
</section>

</body>
</html>
```